Supplement Label Design - Sports Nutrition

Design a sports nutrition/weight loss supplement label that stands out in a crowded space. Supplement bottle size is 200c and label size is 7" x 2.5" approximately. We're looking for a design that emphasizes the products name called VYK. Vyk is an abbreviation for Vigor, Yield & Kinetics. We want VYK to be the center/focus point of the bottle and have a memorable design to it.

Target Market(s)

Men & Women over 18

Industry/Entity Type

Supplement

Font styles to use
Sans Serif
Decorative

Requirements
Must have
• Emphasis on the product name VYK. Serious, Inspirational & Motivational feel to the design, typo & colors. Electrocution/lightning feel to the text. Right hand side of label is our formulation. Left hand side is dedicated to explaining the trifecta formulation idea.
Nice to have
• For example, we like the graphic design of "Drum" energy drinks because you can identify the bottle from a distance and is memorable. We think that less is more and we'd like the design/colors do most of the talking.
Should not have
• Cartroon/animated style.

```html
<!DOCTYPE html>
<html lang="en">
<head>
<meta charset="utf-8">
<title>VYK — Supplement Label System</title>
<link rel="stylesheet" href="https://fonts.googleapis.com/css2?family=Montserrat:wght@400;500;700;800;900&family=Open+Sans:wght@400;600;700&display=swap">
<style>
  :root{
    --page:#ffffff;
    --ink:#1d2433;
    --text-light:#f2f4f8;
    --brand-green:#36e08a;
    --tagline:#2b2b2b;
    --green-a:#3fe85c; --green-b:#5ef07a;
    --violet-a:#a446f0; --violet-b:#e244f2;
    --teal-a:#3cf0b2; --teal-b:#62f5d4;
    --pill:#111318;
    --spark:rgba(235,245,255,.95);
    --spark-blue:rgba(120,170,255,.55);
    --spark-haze:rgba(90,140,255,.22);
  }
  *{box-sizing:border-box;margin:0;padding:0}
  html,body{width:1200px;height:692px;overflow:hidden;background:var(--page)}
  .canvas{position:relative;width:1200px;height:692px;font-family:'Montserrat',sans-serif}

  /* ---------- brand showcase ---------- */
  .brand-mark{position:absolute;left:78px;top:112px;font-size:128px;font-weight:900;letter-spacing:-7px;line-height:1;color:var(--brand-green)}
  .front-row{position:absolute;left:98px;top:262px;display:flex;gap:32px}
  .front-slot{width:126px;height:237px;position:relative}
  .front-slot .band{transform:scale(1.3);transform-origin:0 0}
  .front-slot .band-halo{position:absolute;left:-18px;top:-10px;width:162px;height:257px;
    background:radial-gradient(ellipse 50% 45% at 45% 40%,var(--spark-haze),transparent 72%)}
  .brand-tagline{position:absolute;left:81px;top:545px;font-size:14.5px;font-weight:400;letter-spacing:2.4px;color:var(--tagline)}

  /* ---------- name band (shared front panel) ---------- */
  .band{position:absolute;left:0;top:0;width:97px;height:182px;overflow:hidden}
  .band-shape{position:absolute;inset:0;width:97px;height:182px}
  .band-lightning{position:absolute;inset:0;
    background:
      radial-gradient(ellipse 9% 22% at 34% 6%,var(--spark),transparent 70%),
      radial-gradient(ellipse 14% 10% at 30% 42%,var(--spark),transparent 75%),
      radial-gradient(ellipse 10% 14% at 62% 88%,rgba(235,245,255,.8),transparent 70%),
      linear-gradient(100deg,transparent 30%,rgba(220,235,255,.55) 33%,transparent 36%),
      radial-gradient(ellipse 45% 40% at 32% 40%,var(--spark-blue),transparent 75%),
      radial-gradient(ellipse 30% 30% at 70% 85%,rgba(120,170,255,.35),transparent 75%)}
  .band-name{position:absolute;left:37px;top:84px;transform:translate(-50%,-50%) rotate(-90deg);
    font-size:58px;font-weight:900;letter-spacing:-2px;line-height:1;color:var(--ink);white-space:nowrap}
  .band-tagline{position:absolute;left:82px;top:92px;transform:translate(-50%,-50%) rotate(-90deg);
    background:var(--pill);color:var(--text-light);font-size:3.9px;font-weight:500;letter-spacing:.3px;
    padding:1.4px 3px;border-radius:3px;white-space:nowrap}
  .band-product{position:absolute;left:20px;top:154px;width:56px;background:var(--pill);border-radius:2px;
    text-align:center;color:var(--text-light);padding:1px 0 1.5px}
  .band-product strong{display:block;font-size:6px;font-weight:800;letter-spacing:.2px;line-height:1.1}
  .band-product span{display:block;font-size:3.3px;line-height:1.15;font-weight:400}

  /* ---------- flat labels ---------- */
  .labels{position:absolute;left:618px;top:63px}
  .label{position:absolute;left:0;width:509px;height:182px;overflow:hidden;color:var(--text-light)}
  .label--green{top:0;background:linear-gradient(90deg,#0d1a20,#13242b 55%,#0e1a20)}
  .label--violet{top:192px;background:linear-gradient(90deg,#0a0a0c,#111114 55%,#0a0a0c)}
  .label--teal{top:383px;background:linear-gradient(90deg,#090d36,#121a52 55%,#0b1040)}
  .label-storm{position:absolute;inset:0;background:
    radial-gradient(ellipse 12% 55% at 97% 25%,rgba(190,210,255,.22),transparent 70%),
    radial-gradient(ellipse 14% 35% at 6% 12%,rgba(190,210,255,.16),transparent 70%),
    radial-gradient(ellipse 10% 30% at 72% 90%,rgba(190,210,255,.12),transparent 70%),
    radial-gradient(ellipse 8% 25% at 38% 8%,rgba(190,210,255,.10),transparent 70%)}
  .label-halo{position:absolute;left:176px;top:0;width:160px;height:182px;
    background:radial-gradient(ellipse 45% 50% at 40% 45%,rgba(100,160,255,.35),transparent 75%)}
  .label-name{position:absolute;left:35px;top:31px;font-size:36px;font-weight:900;letter-spacing:-2px;line-height:1}
  .label--green .label-name{color:var(--green-a)}
  .label--violet .label-name{color:var(--violet-a)}
  .label--teal .label-name{color:var(--teal-a)}
  .label-story{position:absolute;left:35px;top:78px;width:140px;font-family:'Open Sans',sans-serif;font-size:3.5px;line-height:5.8px}
  .label-story p{margin-bottom:11.4px}
  .label .band{left:206px}

  .label--green .band,.front-slot--green .band{--accent:var(--green-a);--accent-2:var(--green-b)}
  .label--violet .band,.front-slot--violet .band{--accent:var(--violet-a);--accent-2:var(--violet-b)}
  .label--teal .band,.front-slot--teal .band{--accent:var(--teal-a);--accent-2:var(--teal-b)}

  .facts{position:absolute;left:329px;top:41px;width:161px;font-family:'Open Sans',sans-serif}
  .facts-box{border:.6px solid var(--text-light);padding:1.2px 1.5px}
  .facts-title{font-size:4.6px;font-weight:700;line-height:6px}
  .facts table{width:100%;border-collapse:collapse;font-size:3.1px;line-height:4.9px}
  .facts td{border-bottom:.3px solid rgba(255,255,255,.7);white-space:nowrap}
  .facts td.q{text-align:right;width:14px}
  .facts td.u{text-align:center;width:14px}
  .facts td.d{text-align:right;width:12px}
  .facts tr.blend td{font-weight:700}
  .facts tr.sub td:first-child{padding-left:3px}
  .facts tr.plain td{border-bottom:none}
  .facts-other{font-size:3.1px;line-height:5px}
  .facts-warning{font-size:3.1px;font-weight:700;margin-top:5px}
</style>
</head>
<body>
<main class="canvas">

  <section class="brand">
    <h1 class="brand-mark">VYK</h1>

    <div class="front-row">
      <div class="front-slot front-slot--teal">
        <div class="band-halo" role="img" aria-label="Electric blue glow around the label"></div>
        <div class="band">
          <svg class="band-shape" viewBox="0 0 97 182" aria-hidden="true">
            <rect x="0" y="0" width="72" height="182" fill="var(--accent)"/>
            <rect x="72" y="25" width="25" height="100" fill="var(--accent-2)"/>
            <rect x="0" y="96" width="22" height="86" fill="var(--accent-2)" opacity=".6"/>
          </svg>
          <div class="band-lightning" role="img" aria-label="Lightning bolts striking through the name band"></div>
          <div class="band-name">VYK</div>
          <div class="band-tagline">• Vigor, Yield &amp; Kinetics •</div>
          <div class="band-product"><strong>LOREM IPSUM</strong><span>Lorem ipsum dolor sit<br>amet, consectetur</span></div>
        </div>
      </div>
      <div class="front-slot front-slot--violet">
        <div class="band-halo" role="img" aria-label="Electric blue glow around the label"></div>
        <div class="band">
          <svg class="band-shape" viewBox="0 0 97 182" aria-hidden="true">
            <rect x="0" y="0" width="72" height="182" fill="var(--accent)"/>
            <rect x="72" y="25" width="25" height="100" fill="var(--accent-2)"/>
            <rect x="0" y="96" width="22" height="86" fill="var(--accent-2)" opacity=".6"/>
          </svg>
          <div class="band-lightning" role="img" aria-label="Lightning bolts striking through the name band"></div>
          <div class="band-name">VYK</div>
          <div class="band-tagline">• Vigor, Yield &amp; Kinetics •</div>
          <div class="band-product"><strong>LOREM IPSUM</strong><span>Lorem ipsum dolor sit<br>amet, consectetur</span></div>
        </div>
      </div>
      <div class="front-slot front-slot--green">
        <div class="band-halo" role="img" aria-label="Electric blue glow around the label"></div>
        <div class="band">
          <svg class="band-shape" viewBox="0 0 97 182" aria-hidden="true">
            <rect x="0" y="0" width="72" height="182" fill="var(--accent)"/>
            <rect x="72" y="25" width="25" height="100" fill="var(--accent-2)"/>
            <rect x="0" y="96" width="22" height="86" fill="var(--accent-2)" opacity=".6"/>
          </svg>
          <div class="band-lightning" role="img" aria-label="Lightning bolts striking through the name band"></div>
          <div class="band-name">VYK</div>
          <div class="band-tagline">• Vigor, Yield &amp; Kinetics •</div>
          <div class="band-product"><strong>LOREM IPSUM</strong><span>Lorem ipsum dolor sit<br>amet, consectetur</span></div>
        </div>
      </div>
    </div>

    <p class="brand-tagline">Vigor, Yield &amp; Kinetics</p>
  </section>

  <section class="labels">

    <article class="label label--green">
      <div class="label-storm" role="img" aria-label="Dark storm sky with lightning"></div>
      <div class="label-halo" role="img" aria-label="Electric glow behind the name band"></div>
      <div class="label-name">VYK</div>
      <div class="label-story">
        <p>Lorem ipsum dolor sit amet, consectetur adipiscing elit, sed do eiusmod tempor incididunt ut labore et dolore magna aliqua. Quis ipsum suspendisse ultrices gravida. Risus commodo viverra maecenas accumsan lacus vel facilisis.</p>
        <p>Lorem ipsum dolor sit amet, consectetur adipiscing elit, sed do eiusmod tempor incididunt ut labore et dolore magna aliqua. Quis ipsum suspendisse ultrices gravida. Risus commodo viverra maecenas accumsan lacus vel facilisis.</p>
        <p>Lorem ipsum dolor sit amet, consectetur adipiscing elit, sed do eiusmod tempor incididunt ut labore et dolore magna aliqua. Quis ipsum suspendisse ultrices gravida. Risus commodo viverra maecenas accumsan lacus vel facilisis.</p>
      </div>
      <div class="band">
        <svg class="band-shape" viewBox="0 0 97 182" aria-hidden="true">
          <rect x="0" y="0" width="72" height="182" fill="var(--accent)"/>
          <rect x="72" y="25" width="25" height="100" fill="var(--accent-2)"/>
          <rect x="0" y="96" width="22" height="86" fill="var(--accent-2)" opacity=".6"/>
        </svg>
        <div class="band-lightning" role="img" aria-label="Lightning bolts striking through the name band"></div>
        <div class="band-name">VYK</div>
        <div class="band-tagline">• Vigor, Yield &amp; Kinetics •</div>
        <div class="band-product"><strong>LOREM IPSUM</strong><span>Lorem ipsum dolor sit<br>amet, consectetur</span></div>
      </div>
      <div class="facts">
        <div class="facts-box">
          <div class="facts-title">Supplement Facts</div>
          <table>
            <tr class="plain"><td colspan="4">Serving Size: 2 capsules</td></tr>
            <tr><td colspan="4">Servings Per Container: 30</td></tr>
            <tr><td>Amount per Serving</td><td class="q"></td><td class="u"></td><td class="d">%DV</td></tr>
            <tr><td>Niacin (as niacinamide)</td><td class="q">40</td><td class="u">mg</td><td class="d">250%</td></tr>
            <tr><td>Vitamin B6 (as pyridoxal-5-phosphate)</td><td class="q">8.5</td><td class="u">mg</td><td class="d">500%</td></tr>
            <tr><td>Vitamin B12 (as methylcobalamin)</td><td class="q">12</td><td class="u">mcg</td><td class="d">500%</td></tr>
            <tr class="blend"><td>Proprietary Vigor Blend</td><td class="q">450</td><td class="u">mg</td><td class="d">*</td></tr>
            <tr class="sub"><td>Ashwagandha Root Extract (<i>Withania somnifera</i>)</td><td></td><td></td><td class="d">*</td></tr>
            <tr class="sub"><td>Acetyl L-Carnitine HCl</td><td></td><td></td><td class="d">*</td></tr>
            <tr class="sub"><td>L-Theanine</td><td></td><td></td><td class="d">*</td></tr>
            <tr class="blend"><td>Proprietary Yield Blend</td><td class="q">425</td><td class="u">mg</td><td class="d">*</td></tr>
            <tr class="sub"><td><i>Garcinia cambogia</i> extract (fruit)</td><td></td><td></td><td class="d">*</td></tr>
            <tr class="sub"><td>Yohimbe Bark Extract (<i>Pausinystalia johimbe</i>)</td><td></td><td></td><td class="d">*</td></tr>
            <tr class="sub"><td colspan="3">Capsiva® (capsicum fruit extract)(standardized to 2% capsaicinoids)</td><td class="d">*</td></tr>
            <tr class="blend"><td>Proprietary Kinetics Blend (215 mg Caffeine)</td><td class="q">320</td><td class="u">mg</td><td class="d">*</td></tr>
            <tr class="sub"><td>Green Tea Extract</td><td></td><td></td><td class="d">*</td></tr>
            <tr class="sub"><td>Theobromine</td><td></td><td></td><td class="d">*</td></tr>
            <tr class="sub"><td>Green Coffee Fruit Extract</td><td></td><td></td><td class="d">*</td></tr>
            <tr class="plain"><td colspan="4">*Daily Value (DV) not established</td></tr>
          </table>
        </div>
        <p class="facts-other">Other Ingredients: Rice flour, L-leucine, hypromellose (capsule).</p>
        <p class="facts-warning">Warning: Contains 215 mg of caffeine per serving.</p>
      </div>
    </article>

    <article class="label label--violet">
      <div class="label-storm" role="img" aria-label="Dark storm sky with lightning"></div>
      <div class="label-halo" role="img" aria-label="Electric glow behind the name band"></div>
      <div class="label-name">VYK</div>
      <div class="label-story">
        <p>Lorem ipsum dolor sit amet, consectetur adipiscing elit, sed do eiusmod tempor incididunt ut labore et dolore magna aliqua. Quis ipsum suspendisse ultrices gravida. Risus commodo viverra maecenas accumsan lacus vel facilisis.</p>
        <p>Lorem ipsum dolor sit amet, consectetur adipiscing elit, sed do eiusmod tempor incididunt ut labore et dolore magna aliqua. Quis ipsum suspendisse ultrices gravida. Risus commodo viverra maecenas accumsan lacus vel facilisis.</p>
        <p>Lorem ipsum dolor sit amet, consectetur adipiscing elit, sed do eiusmod tempor incididunt ut labore et dolore magna aliqua. Quis ipsum suspendisse ultrices gravida. Risus commodo viverra maecenas accumsan lacus vel facilisis.</p>
      </div>
      <div class="band">
        <svg class="band-shape" viewBox="0 0 97 182" aria-hidden="true">
          <rect x="0" y="0" width="72" height="182" fill="var(--accent)"/>
          <rect x="72" y="25" width="25" height="100" fill="var(--accent-2)"/>
          <rect x="0" y="96" width="22" height="86" fill="var(--accent-2)" opacity=".6"/>
        </svg>
        <div class="band-lightning" role="img" aria-label="Lightning bolts striking through the name band"></div>
        <div class="band-name">VYK</div>
        <div class="band-tagline">• Vigor, Yield &amp; Kinetics •</div>
        <div class="band-product"><strong>LOREM IPSUM</strong><span>Lorem ipsum dolor sit<br>amet, consectetur</span></div>
      </div>
      <div class="facts">
        <div class="facts-box">
          <div class="facts-title">Supplement Facts</div>
          <table>
            <tr class="plain"><td colspan="4">Serving Size: 2 capsules</td></tr>
            <tr><td colspan="4">Servings Per Container: 30</td></tr>
            <tr><td>Amount per Serving</td><td class="q"></td><td class="u"></td><td class="d">%DV</td></tr>
            <tr><td>Niacin (as niacinamide)</td><td class="q">40</td><td class="u">mg</td><td class="d">250%</td></tr>
            <tr><td>Vitamin B6 (as pyridoxal-5-phosphate)</td><td class="q">8.5</td><td class="u">mg</td><td class="d">500%</td></tr>
            <tr><td>Vitamin B12 (as methylcobalamin)</td><td class="q">12</td><td class="u">mcg</td><td class="d">500%</td></tr>
            <tr class="blend"><td>Proprietary Vigor Blend</td><td class="q">450</td><td class="u">mg</td><td class="d">*</td></tr>
            <tr class="sub"><td>Ashwagandha Root Extract (<i>Withania somnifera</i>)</td><td></td><td></td><td class="d">*</td></tr>
            <tr class="sub"><td>Acetyl L-Carnitine HCl</td><td></td><td></td><td class="d">*</td></tr>
            <tr class="sub"><td>L-Theanine</td><td></td><td></td><td class="d">*</td></tr>
            <tr class="blend"><td>Proprietary Yield Blend</td><td class="q">425</td><td class="u">mg</td><td class="d">*</td></tr>
            <tr class="sub"><td><i>Garcinia cambogia</i> extract (fruit)</td><td></td><td></td><td class="d">*</td></tr>
            <tr class="sub"><td>Yohimbe Bark Extract (<i>Pausinystalia johimbe</i>)</td><td></td><td></td><td class="d">*</td></tr>
            <tr class="sub"><td colspan="3">Capsiva® (capsicum fruit extract)(standardized to 2% capsaicinoids)</td><td class="d">*</td></tr>
            <tr class="blend"><td>Proprietary Kinetics Blend (215 mg Caffeine)</td><td class="q">320</td><td class="u">mg</td><td class="d">*</td></tr>
            <tr class="sub"><td>Green Tea Extract</td><td></td><td></td><td class="d">*</td></tr>
            <tr class="sub"><td>Theobromine</td><td></td><td></td><td class="d">*</td></tr>
            <tr class="sub"><td>Green Coffee Fruit Extract</td><td></td><td></td><td class="d">*</td></tr>
            <tr class="plain"><td colspan="4">*Daily Value (DV) not established</td></tr>
          </table>
        </div>
        <p class="facts-other">Other Ingredients: Rice flour, L-leucine, hypromellose (capsule).</p>
        <p class="facts-warning">Warning: Contains 215 mg of caffeine per serving.</p>
      </div>
    </article>

    <article class="label label--teal">
      <div class="label-storm" role="img" aria-label="Dark storm sky with lightning"></div>
      <div class="label-halo" role="img" aria-label="Electric glow behind the name band"></div>
      <div class="label-name">VYK</div>
      <div class="label-story">
        <p>Lorem ipsum dolor sit amet, consectetur adipiscing elit, sed do eiusmod tempor incididunt ut labore et dolore magna aliqua. Quis ipsum suspendisse ultrices gravida. Risus commodo viverra maecenas accumsan lacus vel facilisis.</p>
        <p>Lorem ipsum dolor sit amet, consectetur adipiscing elit, sed do eiusmod tempor incididunt ut labore et dolore magna aliqua. Quis ipsum suspendisse ultrices gravida. Risus commodo viverra maecenas accumsan lacus vel facilisis.</p>
        <p>Lorem ipsum dolor sit amet, consectetur adipiscing elit, sed do eiusmod tempor incididunt ut labore et dolore magna aliqua. Quis ipsum suspendisse ultrices gravida. Risus commodo viverra maecenas accumsan lacus vel facilisis.</p>
      </div>
      <div class="band">
        <svg class="band-shape" viewBox="0 0 97 182" aria-hidden="true">
          <rect x="0" y="0" width="72" height="182" fill="var(--accent)"/>
          <rect x="72" y="25" width="25" height="100" fill="var(--accent-2)"/>
          <rect x="0" y="96" width="22" height="86" fill="var(--accent-2)" opacity=".6"/>
        </svg>
        <div class="band-lightning" role="img" aria-label="Lightning bolts striking through the name band"></div>
        <div class="band-name">VYK</div>
        <div class="band-tagline">• Vigor, Yield &amp; Kinetics •</div>
        <div class="band-product"><strong>LOREM IPSUM</strong><span>Lorem ipsum dolor sit<br>amet, consectetur</span></div>
      </div>
      <div class="facts">
        <div class="facts-box">
          <div class="facts-title">Supplement Facts</div>
          <table>
            <tr class="plain"><td colspan="4">Serving Size: 2 capsules</td></tr>
            <tr><td colspan="4">Servings Per Container: 30</td></tr>
            <tr><td>Amount per Serving</td><td class="q"></td><td class="u"></td><td class="d">%DV</td></tr>
            <tr><td>Niacin (as niacinamide)</td><td class="q">40</td><td class="u">mg</td><td class="d">250%</td></tr>
            <tr><td>Vitamin B6 (as pyridoxal-5-phosphate)</td><td class="q">8.5</td><td class="u">mg</td><td class="d">500%</td></tr>
            <tr><td>Vitamin B12 (as methylcobalamin)</td><td class="q">12</td><td class="u">mcg</td><td class="d">500%</td></tr>
            <tr class="blend"><td>Proprietary Vigor Blend</td><td class="q">450</td><td class="u">mg</td><td class="d">*</td></tr>
            <tr class="sub"><td>Ashwagandha Root Extract (<i>Withania somnifera</i>)</td><td></td><td></td><td class="d">*</td></tr>
            <tr class="sub"><td>Acetyl L-Carnitine HCl</td><td></td><td></td><td class="d">*</td></tr>
            <tr class="sub"><td>L-Theanine</td><td></td><td></td><td class="d">*</td></tr>
            <tr class="blend"><td>Proprietary Yield Blend</td><td class="q">425</td><td class="u">mg</td><td class="d">*</td></tr>
            <tr class="sub"><td><i>Garcinia cambogia</i> extract (fruit)</td><td></td><td></td><td class="d">*</td></tr>
            <tr class="sub"><td>Yohimbe Bark Extract (<i>Pausinystalia johimbe</i>)</td><td></td><td></td><td class="d">*</td></tr>
            <tr class="sub"><td colspan="3">Capsiva® (capsicum fruit extract)(standardized to 2% capsaicinoids)</td><td class="d">*</td></tr>
            <tr class="blend"><td>Proprietary Kinetics Blend (215 mg Caffeine)</td><td class="q">320</td><td class="u">mg</td><td class="d">*</td></tr>
            <tr class="sub"><td>Green Tea Extract</td><td></td><td></td><td class="d">*</td></tr>
            <tr class="sub"><td>Theobromine</td><td></td><td></td><td class="d">*</td></tr>
            <tr class="sub"><td>Green Coffee Fruit Extract</td><td></td><td></td><td class="d">*</td></tr>
            <tr class="plain"><td colspan="4">*Daily Value (DV) not established</td></tr>
          </table>
        </div>
        <p class="facts-other">Other Ingredients: Rice flour, L-leucine, hypromellose (capsule).</p>
        <p class="facts-warning">Warning: Contains 215 mg of caffeine per serving.</p>
      </div>
    </article>

  </section>
</main>
</body>
</html>
```